Logo for a small law firm
phrase "Trial Lawyers" should appear
Professional
Colby, Fenwick & Lusk
R. Tomasz Colby
3817 SW 58th Avenue Suite 314 Miami, Florida 33155
tomasz@colbylegal.net
The name of the firm should appear at the top and the phrase "Trial Lawyers" below it
rtomaszcolby rtomaszcolby
Yes, of course. The name is Colby, Fenwick & Lusk. I am looking for a professional business logo/tradename for use on all stationery.
VelunoStudioWorks VelunoStudioWorks
Hi Sir/Madam, Can you please tell me the firm name which you want to put in the logo and which kind of logo you want? Thnx.

```html
<!DOCTYPE html>
<html lang="en">
<head>
<meta charset="utf-8">
<title>Colby, Fenwick &amp; Lusk — Letterhead</title>
<link rel="stylesheet" href="https://fonts.googleapis.com/css2?family=Montserrat:wght@500;700;800&display=swap">
<style>
  :root {
    --backdrop: #d9d9d9;
    --paper: #ffffff;
    --navy: #1c2a4f;
    --gold: #c9973a;
    --ink: #1c2a4f;
    --faint: #ececec;
    --footer-text: #c9cfdd;
  }
  * { margin: 0; padding: 0; box-sizing: border-box; }
  html, body {
    width: 1200px;
    height: 816px;
    overflow: hidden;
    background: var(--backdrop);
    font-family: "Montserrat", Arial, sans-serif;
  }
  .stage {
    width: 1200px;
    height: 816px;
    display: flex;
    align-items: center;
    justify-content: center;
  }
  .letterhead {
    position: relative;
    width: 540px;
    height: 764px;
    background: var(--paper);
    box-shadow: 0 6px 22px rgba(0,0,0,0.18);
  }
  .masthead {
    position: absolute;
    top: 40px;
    right: 40px;
    text-align: right;
  }
  .firm-line {
    display: flex;
    align-items: center;
    justify-content: flex-end;
    gap: 7px;
  }
  .firm-line .dot {
    width: 9px;
    height: 9px;
    background: var(--navy);
    border-radius: 50%;
  }
  .firm-name {
    font-weight: 700;
    font-size: 12px;
    color: var(--gold);
    letter-spacing: 0.3px;
    white-space: nowrap;
  }
  .tagline {
    font-weight: 500;
    font-size: 8px;
    color: var(--ink);
    letter-spacing: 1.2px;
    text-transform: uppercase;
    margin-top: 4px;
  }
  .watermark {
    position: absolute;
    top: 230px;
    left: 0;
    width: 100%;
    text-align: center;
    font-weight: 800;
    font-size: 38px;
    color: var(--faint);
    letter-spacing: 1px;
    white-space: nowrap;
  }
  .footer-band {
    position: absolute;
    left: 0;
    bottom: 0;
    width: 100%;
    height: 40px;
    background: var(--navy);
    border-top: 3px solid var(--gold);
    display: flex;
    align-items: center;
    justify-content: center;
    gap: 14px;
    font-size: 7.5px;
    font-weight: 500;
    color: var(--footer-text);
    letter-spacing: 0.3px;
    white-space: nowrap;
  }
  .footer-band .sep { color: var(--gold); }
</style>
</head>
<body>
  <main class="stage">
    <section class="letterhead">
      <header class="masthead">
        <div class="firm-line">
          <span class="dot"></span>
          <span class="firm-name">Colby, Fenwick &amp; Lusk</span>
        </div>
        <div class="tagline">Trial Lawyers</div>
      </header>

      <div class="watermark" aria-hidden="true">Colby, Fenwick &amp; Lusk</div>

      <footer class="footer-band">
        <span>1290 Harbor Lane Suite 8 Coral Gables, FL 33134</span>
        <span class="sep">|</span>
        <span>T (305) 555-0172</span>
        <span class="sep">|</span>
        <span>office@cfltrial.com</span>
      </footer>
    </section>
  </main>
</body>
</html>
```